Keltrane Systems Brochure Template Design

Design Brief for Keltrane Systems Ltd

Keltrane Systems Ltd requires a sales brochure template. It needs be a word document (so possibly a watermark design) so text and images can be inserted into to create various product brochures as required. We would like the design to be based on our logo which is on our website : www.keltrane-example.com .

I do not require a traditional looking Print Brochure.

What I require is a Designed "Front Page", a Designed "Back Page" and a designed "Insert Page" that I can add Photos, text and specifications with MS Office. Some of our products can have 3, 4 & 5 pages.

Please see our OLD Looking Brochures on www.keltrane-example.com under Products that I want to change with a Modern & Fresh look.

Example
http://www.keltrane-example.com/products/brochures/keltrane_mx410_brochure.pdf
http://www.keltrane-example.com/products/brochures/keltrane_rt5800_brochure.pdf
http://www.keltrane-example.com/products/brochures/keltrane_quikfold470_brochure.pdf

I hope you understand what I am looking for and I look forward to your submissions.

Background about Keltrane Systems Ltd:
Keltrane Systems is an automation company that has been in existence since 1991. See the following link for a brief timeline history: http://www.keltrane-example.com/about/index.html .

Our website should tell you all you need to know about us from a starting point. If you have any further questions please just ask.

We have supplied .png & .psd images of our logo.

Regards,

Keltrane Systems
Updates

Originally we overlooked to Guarantee Payment which has now been corrected. This project is still live with "Payment Guaranteed".

I would appreciate if you could review our brief with the view to submitting your design. 

I look forward to your submissions.

I do not require a traditional looking PrintBrochure. Also a  "watermark" is not absolutely necessary.

What I require is a Designed"Front Page", a Designed "Back Page" and a Designed "Insert Page(s)" that I can addPhotos, text and specifications via MS Word. Some of our products can have 3, 4 & 5pages of technical specifications and photos. 

Please see our OLD LookingBrochures on www.keltrane-example.com under Products that I want to change with a Modern& Fresh look. 

Examples of our Old "Tired" brochures

I hope you understand what I amlooking for and I look forward to your submission.

If you have any questions please do not hesitate to contact me. 

BestRegards, 

Gerald

I have extended the deadline as I was hoping to get some additional Creative Designs so that I could make a decision.

Please consider this please and I look forward to some interesting submissions.

thank you in advance.

Reason: Due to unforeseen circumstances, I have been away for a while. Sorry for not advising you of this. I have not been gripped by any one design so far and I would respectfully request if you could re-engage on this project so that we can get a design that appeals to us. I thank you all for your efforts to date and I look forward to receiving some more exciting designs. Thanking you in advance. Best Regards, Gerald

Industry/Entity Type

It Company

Requirements
Must have
• Please read the update below.
I am looking for at minimum of 3 "separate" designed pages that can be made in an A4 or smaller format.
I do not want a traditional multi-page folded brochure. I think our message was not clearly understood or we have communicated badly.

I need: -
Page 1 as a FRONT Page where I can show our logo, a picture and title of a product.
Page 2,3 or 4 will be an INSERT Page(s) where we can add technical specifications, description of the product, some pictures etc.
BACK Page will have our Contact address details, Building Photo and our Distributors details.

I hope that this is now clearer and I hope to receive your submissions.

Thanking you in advance

Keltrane

```html
<!DOCTYPE html>
<html lang="en">
<head>
<meta charset="utf-8">
<title>Keltrane Systems – Brochure Template</title>
<link rel="stylesheet" href="https://fonts.googleapis.com/css2?family=Caladea&family=Didact+Gothic&family=Questrial&display=swap">
<style>
:root{
  --canvas:#ffffff;
  --page:#ffffff;
  --ink:#1a1a1a;
  --body:#4a4a4a;
  --brand:#1f4f96;
  --bar:#1d4d94;
  --network-a:#2e4f93;
  --network-b:#e9ecf3;
  --photo-a:#1f2f6a;
  --photo-b:#c8ccd8;
}
*{box-sizing:border-box;margin:0;padding:0}
html,body{width:1200px;height:900px;overflow:hidden;background:var(--canvas)}
body{position:relative;font-family:"Didact Gothic",sans-serif;color:var(--ink)}
.board-title{position:absolute;top:72px;left:0;width:1200px;text-align:center;font-family:"Caladea",serif;font-size:20px;color:#111}
.page{position:absolute;width:242px;height:313px;background:var(--page);box-shadow:1px 2px 5px rgba(0,0,0,.45);overflow:hidden}
.caption{position:absolute;width:242px;text-align:center;font-family:"Caladea",serif;font-size:14px;color:#111}
.bar{position:absolute;top:13px;left:15px;width:212px;height:5px;background:var(--bar)}
.network{position:absolute;background:radial-gradient(circle at 60% 50%,var(--network-a) 0%,#6d83b6 35%,var(--network-b) 80%,transparent 100%)}
.photo{position:absolute;background:linear-gradient(160deg,var(--photo-b) 0%,#9aa3bd 40%,var(--photo-a) 100%)}
.brand{position:absolute;display:flex;align-items:center;gap:4px;font-family:"Questrial",sans-serif;color:#222}
.brand .mark{width:10px;height:10px;background:#222}
.brand .name{font-size:8px;letter-spacing:1px}
.tiny{font-size:4px;line-height:5.3px;color:var(--body)}
.head{font-size:5.5px;font-weight:bold;color:var(--brand);margin-bottom:2px}
ul.tiny{padding-left:6px}
.block{position:absolute;left:15px;width:212px}
</style>
</head>
<body>
<h1 class="board-title">Brochure Design created in Word Format</h1>

<!-- Front cover -->
<section class="page" style="left:225px;top:118px;background:linear-gradient(90deg,#fff,#f0f0f0)">
  <div class="network" style="left:-30px;top:10px;width:150px;height:300px" role="img" aria-label="Blue molecular network illustration"></div>
  <div class="brand" style="left:168px;top:30px"><span class="mark"></span><span class="name">KELTRANE</span></div>
  <div style="position:absolute;left:168px;top:212px;font-size:12px;font-weight:bold;color:#222">RT-5800<sup style="font-size:6px">©</sup></div>
  <div class="tiny" style="position:absolute;left:168px;top:232px;color:#333">Specification Document</div>
</section>
<div class="caption" style="left:225px;top:442px">Front Cover Page</div>

<!-- Inside page 1 -->
<section class="page" style="left:480px;top:118px">
  <div class="bar"></div>
  <div class="block" style="top:32px">
    <div style="font-size:13px;font-weight:bold;color:var(--brand)">RT-5800<sup style="font-size:6px">©</sup></div>
    <div style="font-size:7px;color:var(--brand)">CD/DVD Sleever</div>
  </div>
  <div class="photo" style="left:15px;top:58px;width:212px;height:113px" role="img" aria-label="Photo of the sleever machine"></div>
  <div class="block" style="top:175px">
    <p style="font-size:7.2px;line-height:8.4px;color:var(--brand);margin-bottom:4px">Keltrane's, all NEW, RT-5800 CD/DVD sleever has been designed to address the growing demand for mid to high-end automated sleeving solutions.</p>
    <p class="tiny" style="margin-bottom:3px">The RT-5800 offers a significant cost performance alternative over other sleevers currently available on the market. Its unique modular design allows you to choose from the full range of optional extra stations as and when you need them.</p>
    <p class="tiny" style="margin-bottom:3px">The RT-5800 is capable of handling a wide variety of sleeve types for 120mm (and optionally 80mm &amp; business card) CDs at rates of up to 75 sleeves per minute. Sleeve types include Card, Paper (with/without flap), Polypropylene (with/without flap), Spunbond and Safety Sleeve.</p>
    <p class="tiny" style="margin-bottom:3px">Unlike its competitors, the Keltrane RT-5800 has an entirely modular design meaning you get exactly what you need as you need it. Further additional stations can be added on-site within hours so that your sleever simply develops as your demands change.</p>
    <p class="tiny">A key advantage of the RT-5800 is its innovative user-friendly design. The machine operators require minimal training; non-technical personnel can operate the RT-5800 with the set-up and product changeover being accomplished in minutes, not hours.</p>
  </div>
</section>
<div class="caption" style="left:480px;top:442px">Inside Page 1</div>

<!-- Inside page 2 -->
<section class="page" style="left:735px;top:118px">
  <div class="bar"></div>
  <div class="block" style="top:30px">
    <div class="head">Features</div>
    <ul class="tiny">
      <li>Multi-sleeve handling: Card, Paper (with or without flap fold), Polypropylene (with or without flap tuck), Spunbond and Safety Sleeve. Keltrane can quickly validate other sleeve types upon request.</li>
      <li>Up to 75 sleeves per minute.</li>
      <li>Rapid changeover between the standard sleeve types.</li>
      <li>Small footprint.</li>
      <li>Mechanical Index Drive.</li>
      <li>Mechanical Pick and Place for Sleeves, Booklet and CD's</li>
      <li>Multi spindle changer.</li>
      <li>Accumulating conveyor (single, batch or continuous feed).</li>
    </ul>
  </div>
  <div class="photo" style="left:15px;top:97px;width:212px;height:113px" role="img" aria-label="Photo of the sleever machine with conveyor"></div>
  <div class="block" style="top:214px">
    <div class="head">Optional Modules</div>
    <ul class="tiny">
      <li>Automatic 6 spindle changer.</li>
      <li>Flap folding for gummed paper sleeves.</li>
      <li>Booklet insertion.</li>
      <li>Flap tuck-in of Polypropylene sleeves.</li>
      <li>Safety Sleeves.</li>
      <li>Cold melt Gluing system for Paper Sleeves.</li>
      <li>Full Flap for Card Sleeves</li>
      <li>Business Card Option</li>
      <li>80mm CD Option</li>
      <li>Disc orientation.</li>
      <li>CD ID code identification.</li>
      <li>Security Seal Applicator.</li>
    </ul>
  </div>
</section>
<div class="caption" style="left:735px;top:442px">Inside Page 2</div>

<!-- Inside page 3 -->
<section class="page" style="left:225px;top:487px">
  <div class="bar"></div>
  <div class="block" style="top:30px">
    <div class="head">Benefits</div>
    <ul class="tiny" style="margin-bottom:3px">
      <li>High capacity at an affordable price.</li>
      <li>Rapid product changeover.</li>
      <li>Small footprint – easily integrated.</li>
      <li>Simple operation by non-technical personnel.</li>
      <li>Fully customisable.</li>
      <li>Low maintenance due to innovative design.</li>
      <li>Easily upgraded.</li>
      <li>Labour cost reduction.</li>
      <li>Low energy requirement (power and air).</li>
      <li>Off-the-shelf standard spare parts (available from leading suppliers worldwide).</li>
    </ul>
    <div class="head">Specification</div>
    <ul class="tiny">
      <li><b>Weight:</b> Approx. 300kg.</li>
      <li><b>Dimensions:</b> Approx. 2200mm long x 1500mm high x 800mm wide (net of conveyors).</li>
      <li><b>Energy Requirements:</b> 220/110 VAC 50/60Hz, Single Phase 16A, 60-80psi with 8-10 CFM.</li>
    </ul>
  </div>
</section>
<div class="caption" style="left:225px;top:810px">Inside Page 3</div>

<!-- Back cover -->
<section class="page" style="left:480px;top:487px;background:linear-gradient(180deg,#fff,#f2f2f2)">
  <div class="brand" style="left:20px;top:24px"><span class="mark" style="width:8px;height:8px"></span><span class="name" style="font-size:6.5px">KELTRANE</span></div>
  <div class="network" style="left:80px;top:110px;width:200px;height:200px" role="img" aria-label="Blue molecular network illustration"></div>
  <div class="tiny" style="position:absolute;left:20px;top:44px;color:#333">
    <p style="margin-bottom:4px">For further information, please contact:</p>
    <p><b>Keltrane Ltd.</b></p>
    <p>Harlow Enterprise Park</p><p>Millbrook Road</p><p>Dunmere</p><p>Co. Westfield</p><p>Ireland</p>
    <p>Tel: + 000 1 555 0142</p><p>Fax: + 000 1 555 0143</p><p>Email: info@keltrane-example.com</p>
    <p style="margin-top:4px"><b>Keltrane USA</b></p>
    <p>14 Alder Lane</p><p>Fairhaven</p><p>ST 00000</p><p>USA</p>
    <p>Tel: + 1 000 555 0171</p><p>Fax: + 1 000 555 0172</p><p>Email: info@keltrane-example.com</p>
  </div>
  <div style="position:absolute;left:20px;top:260px;font-size:5.5px;color:#333">www.keltrane-example.com</div>
  <div class="tiny" style="position:absolute;left:20px;top:273px;font-size:3px;color:#333"><b>© Keltrane Ltd. / RT-5800.</b> Keltrane reserve the right to change specifications without notice.</div>
</section>
<div class="caption" style="left:480px;top:810px">Back Cover Page</div>
</body>
</html>
```